Boost Your Sales 100% In Prime Picks 2013 With The Velmora 300

Please vist www.brightmerrow.net, use all the images of the current advertisers there on the Home page and create a better flyer from this attached old flyer.

Industry/Entity Type

Sales

```html
<!DOCTYPE html>
<html lang="en">
<head>
<meta charset="utf-8">
<title>Prime Picks 2013 – Velmora 300</title>
<link href="https://fonts.googleapis.com/css2?family=Anton&family=Arimo:wght@400;700&family=Varela+Round&display=swap" rel="stylesheet">
<style>
  :root{
    --ink:#231f20;
    --sky:#2ea9df;
    --sky-light:#63c3ee;
    --panel-top:#d6eef9;
    --panel-bottom:#7fcdf0;
    --red:#e3202a;
    --yellow:#fff200;
    --cream:#f3eaa6;
    --text:#1c1c1c;
  }
  *{margin:0;padding:0;box-sizing:border-box}
  html,body{width:846px;height:1200px;overflow:hidden;background:#fff}
  .flyer{position:relative;width:846px;height:1200px;overflow:hidden;
    background:linear-gradient(180deg,var(--sky) 0%,var(--sky-light) 70%);
    font-family:"Arimo",Arial,sans-serif}
  .backdrop{position:absolute;left:0;top:0}
  .tagline{position:absolute;top:86px;font-family:"Varela Round",Arial,sans-serif;
    color:var(--cream);font-size:23px;line-height:25px}
  .tagline--stop{left:163px}
  .tagline--start{left:556px}
  .icon{position:absolute}
  .icon--stop{left:66px;top:78px;width:92px;height:74px;border-radius:50%;
    background:radial-gradient(circle,#e8393c 0 55%,#b9b9b9 56%)}
  .icon--start{left:432px;top:84px;width:112px;height:66px;border-radius:6px;
    background:linear-gradient(180deg,#59b947,#2f8a35)}
  .burst{position:absolute;background:var(--red);transform:rotate(-8deg)}
  .burst--left{left:38px;top:212px;width:368px;height:236px}
  .burst--right{left:452px;top:282px;width:348px;height:266px}
  .shout{position:absolute;font-family:"Anton",Impact,sans-serif;color:var(--yellow);
    transform:rotate(-8deg);transform-origin:left top;white-space:nowrap;
    text-shadow:3px 3px 0 #3a2a10,-1px -1px 0 #3a2a10,1px -1px 0 #3a2a10,-1px 1px 0 #3a2a10}
  .shout--join{left:122px;top:222px;font-size:30px}
  .shout--brand{left:40px;top:262px;font-size:46px}
  .shout--headline{left:56px;top:300px;font-size:96px;letter-spacing:1px}
  .shout--boost{left:486px;top:348px;font-size:60px}
  .shout--sub{left:490px;top:404px;font-size:40px}
  .shout--percent{left:528px;top:434px;font-size:86px}
  .panel{position:absolute;top:533px;height:260px;padding:34px 14px 0;
    background:linear-gradient(180deg,var(--panel-top),var(--panel-bottom));
    color:var(--text);font-size:19.5px;line-height:25px}
  .panel--guarantee{left:30px;width:380px}
  .panel--guarantee strong{font-weight:700}
  .panel--sponsor{left:422px;width:378px;padding-top:40px;font-family:"Varela Round",Arial,sans-serif}
  .card{display:inline-block;width:70px;height:40px;vertical-align:-6px;margin-left:6px;
    border-radius:4px;background:linear-gradient(135deg,#e9e3b8,#b9b07a)}
  .collage{position:absolute;left:0;top:720px}
</style>
</head>
<body>
<div class="flyer">
  <svg class="backdrop" width="846" height="560" viewBox="0 0 846 560" aria-hidden="true">
    <path d="M0 0H846V330Q600 360 420 410T0 470Z" fill="var(--ink)"/>
  </svg>

  <div class="icon icon--stop" role="img" aria-label="Cartoon stop sign mascot with pointing hand"></div>
  <p class="tagline tagline--stop">offering any more<br>"?%" Discount</p>
  <div class="icon icon--start" role="img" aria-label="Green start button with clicking hand cursor"></div>
  <p class="tagline tagline--start">making much more<br>real money...</p>

  <div class="burst burst--left"></div>
  <div class="burst burst--right"></div>
  <p class="shout shout--join">Join Now</p>
  <p class="shout shout--brand">velmora 300 in</p>
  <p class="shout shout--headline">PRIME PICKS 2013</p>
  <p class="shout shout--boost">We Boost</p>
  <p class="shout shout--sub">your sale upto</p>
  <p class="shout shout--percent">100%</p>

  <div class="panel panel--guarantee">
    <strong>We Guarantee you make more money with our program or money back!</strong><br>
    Call your agent now or<br>call 1-888-555-0142 to<br>locate your agent.
  </div>
  <div class="panel panel--sponsor">
    This Prime Picks 2013 summer promotion is proudly sponsored by the participating business entities and always Brightmerrow.
    Shop, Save N Get Bouns with<span class="card" role="img" aria-label="Membership card"></span>
  </div>

  <svg class="collage" width="846" height="480" viewBox="0 0 846 480" role="img" aria-label="Collage of circular product photos from participating advertisers: toys, gadgets, shoes, handbags, cosmetics, coins, food and fashion">
    <g fill="var(--ink)">
      <circle cx="60" cy="140" r="75"/><circle cx="160" cy="95" r="80"/><circle cx="290" cy="150" r="70"/>
      <circle cx="400" cy="120" r="75"/><circle cx="530" cy="100" r="70"/><circle cx="660" cy="80" r="70"/>
      <circle cx="780" cy="80" r="70"/><circle cx="810" cy="150" r="60"/>
      <rect x="0" y="130" width="846" height="350"/>
    </g>
    <circle cx="160" cy="95" r="68" fill="#4f86b8"/>
    <circle cx="42" cy="130" r="42" fill="#cfd6dc"/>
    <circle cx="268" cy="175" r="55" fill="#c84a3a"/>
    <circle cx="170" cy="200" r="58" fill="#7aa6c8"/>
    <circle cx="60" cy="260" r="70" fill="#d8d2c4"/>
    <circle cx="440" cy="110" r="55" fill="#3a4e6a"/>
    <circle cx="548" cy="112" r="45" fill="#b8303a"/>
    <circle cx="650" cy="82" r="52" fill="#8a6a4a"/>
    <circle cx="798" cy="75" r="52" fill="#5f8cb8"/>
    <circle cx="360" cy="210" r="68" fill="#d9d4cc"/>
    <circle cx="485" cy="195" r="45" fill="#3f4a55"/>
    <circle cx="600" cy="205" r="60" fill="#d8d8d0"/>
    <circle cx="760" cy="210" r="90" fill="#d45a2a"/>
    <circle cx="280" cy="320" r="70" fill="#7a5a3c"/>
    <circle cx="120" cy="390" r="100" fill="#5a8fc0"/>
    <circle cx="420" cy="325" r="50" fill="#c9c9c9"/>
    <circle cx="505" cy="330" r="55" fill="#5d86bd"/>
    <circle cx="640" cy="345" r="60" fill="#e8e2da"/>
    <circle cx="780" cy="355" r="65" fill="#eae4dc"/>
    <circle cx="300" cy="450" r="60" fill="#5d8fc2"/>
    <circle cx="430" cy="450" r="55" fill="#e4e4e4"/>
    <circle cx="545" cy="455" r="60" fill="#d8e2ea"/>
    <circle cx="680" cy="470" r="60" fill="#5a3424"/>
    <circle cx="800" cy="470" r="45" fill="#c83c3a"/>
  </svg>
</div>
</body>
</html>
```